Equity, Effectiveness and Efficiency in charitable food relief sector

I am undertaking my PhD in food policy in the charitable food relief sector, specifically investigating the factors (supply, demand and capacity) that affect the introduction of nutrition policy and in turn, affect the sector's ability to achieve equity, effectiveness and efficiency.

I need a graphic device that incorporates this central idea of Equity, Effectiveness and Efficiency, and how the factors of supply, demand and capacity interact. There are sub-factors within supply (1-6), demand (7-10) and capacity (11 - 15). All these details are shown in the attached figure (Basic figure_Eq Effec Effic and factors.jpg)

This figure (Basic figure_Eq Effec Effic and factors.jpg) contains all the information I need in a graphic but I need something that is more visually appealing, and that can link the ideas in a format other than a table. The final graphic will outline how the food relief sector balances the core objectives of equity, effectiveness and efficiency with the factors (and sub-factors) of supply, demand and capacity.

```html
<!DOCTYPE html>
<html lang="en">
<head>
<meta charset="utf-8">
<title>Triple E – Factors Affecting the Introduction of Nutrition Policy</title>
<link rel="stylesheet" href="https://fonts.googleapis.com/css2?family=Montserrat:wght@300;400;500;600;700;800&display=swap">
<style>
  :root {
    --green: #8dc63f;
    --green-light: #a1cd4b;
    --green-dark: #76a63a;
    --lime-line: #e3e620;
    --lime: #e5e51c;
    --yellow: #ffdd00;
    --orange: #f7722f;
    --red: #e8231a;
    --ink: #111111;
    --white: #ffffff;
  }
  html, body { margin: 0; padding: 0; overflow: hidden; }
  body { width: 1200px; height: 2400px; background: var(--white); }
  .poster {
    position: relative; width: 1200px; height: 2400px; overflow: hidden;
    background: var(--white); font-family: "Montserrat", Arial, sans-serif; color: var(--ink);
  }
  .side-band { position: absolute; left: 0; top: 0; width: 214px; height: 2215px; background: var(--green); }
  .side-title {
    position: absolute; left: 65px; top: 970px; transform: translate(-50%, -50%) rotate(-90deg);
    white-space: nowrap; color: var(--white); font-weight: 700; font-size: 21px; letter-spacing: 0.2px;
  }
  .connectors { position: absolute; left: 0; top: 0; }
  .hero-block { position: absolute; left: 585px; top: 0; width: 615px; height: 458px; background: var(--green); overflow: hidden; }
  .hero-block .shade { position: absolute; background: var(--green-light); }
  .hero-title {
    position: absolute; left: 287px; top: 80px; margin: 0;
    font-size: 49px; font-weight: 800; color: var(--green-dark); letter-spacing: 1px; line-height: 1;
  }
  .big-e { position: absolute; left: 287px; top: 135px; }
  .e-word {
    position: absolute; left: 611px; margin: 0; color: var(--white);
    font-weight: 400; font-size: 62px; letter-spacing: 2px; line-height: 1;
  }
  .objective-band {
    position: absolute; left: 214px; top: 468px; width: 986px; height: 59px; background: var(--green);
    color: var(--white); font-weight: 700; font-size: 38px; line-height: 59px; padding-left: 72px;
    box-sizing: border-box; letter-spacing: 0.5px; word-spacing: 4px;
  }
  .factor { position: absolute; left: 300px; }
  .factor h2 { margin: 0 0 18px; font-size: 46px; font-weight: 600; line-height: 1; letter-spacing: 0.5px; }
  .factor ul { margin: 0; padding: 0; list-style: none; }
  .factor li { position: relative; font-size: 34px; line-height: 43.2px; padding-left: 40px; letter-spacing: 1px; }
  .factor li.item::before {
    content: ""; position: absolute; left: 2px; top: 16px; width: 13px; height: 13px; border-radius: 50%; background: var(--ink);
  }
  .factor li.sub { padding-left: 76px; }
  .swatches { position: absolute; left: 233px; display: flex; gap: 18px; }
  .swatches span { width: 62px; height: 62px; display: block; }
  .note {
    position: absolute; background: var(--red); color: var(--white);
    border-radius: 50px 0 0 50px; box-sizing: border-box; padding-left: 47px;
    font-weight: 800; font-size: 33px; line-height: 43.2px; letter-spacing: 0.3px;
  }
  .note p { margin: 0; }
  .footer {
    position: absolute; left: 0; top: 2228px; width: 1200px; height: 172px; background: var(--green-dark);
    color: var(--white); font-weight: 700; font-size: 22px;
  }
  .footer p { margin: 0; position: absolute; left: 240px; top: 38px; }
</style>
</head>
<body>
<div class="poster">
  <div class="side-band"></div>
  <div class="side-title">Factors Affecting the Introduction of Nutrition Policy</div>

  <div class="hero-block">
    <div class="shade" style="left:130px;top:0;width:485px;height:342px;"></div>
    <div class="shade" style="left:0;top:0;width:243px;height:215px;background:var(--green);"></div>
    <div class="shade" style="left:243px;top:0;width:115px;height:215px;background:var(--green);"></div>
    <div class="shade" style="left:472px;top:0;width:120px;height:215px;background:var(--green);"></div>
    <div class="shade" style="left:358px;top:0;width:114px;height:215px;"></div>
  </div>

  <svg class="connectors" width="1200" height="2215" viewBox="0 0 1200 2215" aria-hidden="true">
    <g stroke="var(--lime-line)" stroke-width="3" fill="none">
      <path d="M98 162 V1598"/>
      <path d="M98 162 H260 M98 282 H260 M98 402 H260 M98 606 H260 M98 1138 H260 M98 1598 H260"/>
      <path d="M543 162 H600 M543 282 H600 M543 402 H600"/>
    </g>
    <g fill="var(--lime-line)">
      <circle cx="260" cy="162" r="6.5"/><circle cx="260" cy="282" r="6.5"/><circle cx="260" cy="402" r="6.5"/>
      <circle cx="260" cy="606" r="6.5"/><circle cx="260" cy="1138" r="6.5"/><circle cx="260" cy="1598" r="6.5"/>
      <circle cx="543" cy="162" r="6.5"/><circle cx="543" cy="282" r="6.5"/><circle cx="543" cy="402" r="6.5"/>
    </g>
  </svg>

  <h1 class="hero-title">TRIPLE E</h1>
  <svg class="big-e" width="230" height="298" viewBox="0 0 230 298" aria-label="Large letter E">
    <path fill="var(--green-dark)" d="M0 0 H225 V57 H65 V115 H206 V177 H65 V240 H228 V297 H0 Z"/>
  </svg>
  <p class="e-word" style="top:136px;">QUITY</p>
  <p class="e-word" style="top:256px;">FFECTIVENESS</p>
  <p class="e-word" style="top:376px;">FFICIENCY</p>

  <div class="objective-band">• Equity • Effectiveness • Efficiency</div>

  <section class="factor" style="top:585px;">
    <h2>Supply</h2>
    <ul>
      <li class="item">Uncertain Material Supply</li>
      <li class="item">Uncertain Monetary Supply</li>
      <li class="item">Limited Food Supply</li>
      <li class="item">Perishability</li>
      <li class="item">Donor Constraints</li>
      <li class="item">Donor Relationships</li>
    </ul>
  </section>

  <div class="swatches" style="top:982px;">
    <span style="background:var(--green)"></span><span style="background:var(--lime)"></span><span style="background:var(--yellow)"></span><span style="background:var(--orange)"></span><span style="background:var(--red)"></span>
  </div>

  <section class="factor" style="top:1117px;">
    <h2>Demand</h2>
    <ul>
      <li class="item">Uncertain Demand</li>
      <li class="item">Limited Demand Visibility</li>
      <li class="item">Client Choice</li>
      <li class="item">Food Wastage</li>
    </ul>
  </section>

  <div class="swatches" style="top:1425px;">
    <span style="background:var(--green)"></span><span style="background:var(--lime)"></span><span style="background:var(--yellow)"></span><span style="background:var(--orange)"></span><span style="background:var(--red)"></span>
  </div>

  <section class="factor" style="top:1574px;">
    <h2>Capacity</h2>
    <ul>
      <li class="item">Storage</li>
      <li class="sub">a. Cold</li>
      <li class="sub">b. Warehouse</li>
      <li class="item">Transportation</li>
      <li class="item">Workforce</li>
      <li class="sub">a. Volunteers</li>
      <li class="sub">b. Expertise and Training</li>
      <li class="sub">c. Attitudes and Beliefs</li>
      <li class="sub">d. Collaboration</li>
      <li class="sub">e. Executive Support</li>
      <li class="item">External Stakeholders</li>
      <li class="item">Budget</li>
    </ul>
  </section>

  <aside class="note" style="left:787px;top:757px;width:413px;height:470px;padding-top:32px;">
    <p>Factors<br>that affect the<br>introduction<br>of nutrition policy<br>and in turn, affect<br>the sector's ability<br>to achieve equity,<br>effectiveness<br>and efficiency.</p>
  </aside>

  <aside class="note" style="left:783px;top:1327px;width:417px;height:560px;padding-left:51px;padding-top:42px;">
    <p>How the food<br>relief sector<br>balances the core<br>objectives of<br>equity,<br>effectiveness and<br>efficiency with<br>he factors and<br>sub-factors of<br>supply, demand<br>and capacity.</p>
  </aside>

  <footer class="footer">
    <p>PhD in Food Policy Asssesment byYour name &amp; Department</p>
  </footer>
</div>
</body>
</html>
```